Business Card Design

Personal training studio. My colors are burnt orange and grey. Specializing in group training and total body composition change. Nutritional consultant and contest prep.

Target Market(s)

My audience are people who are looking for total body composition change as well as knowledge on how to effectively receive results in the gym that they are a member of.

Industry/Entity Type

Training

Contact Information for Business Card

Dr. Maris Thackery
Marisjthackery@plumvane.com
3129071436
2815 west Brell ave.
Marrowfield Illinois 60948

Colors
f37122
aaaaaa

Requirements
Must have
• Animphasis on gaining knowledge that will sustain them for a life time. Healthy results and notice me results.
Nice to have
• Card should correlate with the colors of the studio. Orange and grey. With black flooring with orange speckles in it.

```html
<!DOCTYPE html>
<html lang="en">
<head>
<meta charset="utf-8">
<title>Keystone Body Lab – Business Card</title>
<link href="https://fonts.googleapis.com/css2?family=PT+Sans:wght@400;700&display=swap" rel="stylesheet">
<style>
  :root {
    --backdrop-light: #d6d6d6;
    --backdrop-dark: #6e6e6e;
    --card-black: #0d0d0d;
    --card-charcoal: #1c1c1c;
    --burnt-orange: #f37122;
    --orange-light: #f6a45c;
    --ink-white: #f2f2f2;
    --studio-grey: #aaaaaa;
  }
  * { box-sizing: border-box; margin: 0; padding: 0; }
  html, body {
    width: 1200px;
    height: 900px;
    overflow: hidden;
  }
  body {
    background: radial-gradient(ellipse at 50% 45%, var(--backdrop-light) 0%, #a9a9a9 55%, var(--backdrop-dark) 100%);
    font-family: "PT Sans", Verdana, sans-serif;
    position: relative;
  }
  .card {
    position: absolute;
    left: 310px;
    width: 580px;
    height: 330px;
    background: radial-gradient(ellipse at 30% 40%, var(--card-charcoal) 0%, var(--card-black) 70%);
    box-shadow: 0 14px 30px rgba(0,0,0,0.45);
    overflow: hidden;
  }
  .card--front { top: 60px; }
  .card--back { top: 480px; }

  .brand {
    display: flex;
    align-items: center;
    gap: 16px;
  }
  .brand__mark {
    border-radius: 50%;
    background: linear-gradient(135deg, var(--orange-light), var(--burnt-orange));
    flex: none;
  }
  .brand__name {
    color: var(--ink-white);
    font-weight: 700;
    text-transform: uppercase;
    letter-spacing: 2px;
    line-height: 1.1;
    white-space: nowrap;
  }

  .card--front .brand {
    position: absolute;
    left: 50%;
    top: 50%;
    transform: translate(-50%, -50%);
  }
  .card--front .brand__mark { width: 120px; height: 120px; }
  .card--front .brand__name { font-size: 34px; }

  .card--back .brand {
    position: absolute;
    right: 34px;
    top: 74px;
  }
  .card--back .brand__mark { width: 62px; height: 62px; }
  .card--back .brand__name { font-size: 20px; }

  .holder-name {
    position: absolute;
    left: 34px;
    top: 26px;
    color: var(--ink-white);
    font-size: 18px;
    font-weight: 700;
    font-style: italic;
  }
  .contact {
    position: absolute;
    left: 34px;
    top: 160px;
    list-style: none;
    color: var(--ink-white);
    font-size: 17px;
    line-height: 1.55;
  }
  .contact__item {
    display: flex;
    align-items: center;
    gap: 10px;
    white-space: nowrap;
  }
  .contact__icon {
    width: 16px;
    height: 16px;
    flex: none;
    fill: var(--studio-grey);
  }
  .accent-band {
    position: absolute;
    left: 0;
    bottom: 0;
    width: 100%;
    height: 16px;
    background: linear-gradient(90deg, #d45a12, var(--burnt-orange) 60%, #f9a43a);
  }
</style>
</head>
<body>

  <section class="card card--front" aria-label="Card front">
    <div class="brand">
      <span class="brand__mark"></span>
      <span class="brand__name">Keystone<br>Body Lab</span>
    </div>
  </section>

  <section class="card card--back" aria-label="Card back">
    <p class="holder-name">Dr. Maris Thackery</p>

    <div class="brand">
      <span class="brand__mark"></span>
      <span class="brand__name">Keystone<br>Body Lab</span>
    </div>

    <ul class="contact">
      <li class="contact__item">
        <svg class="contact__icon" viewBox="0 0 16 16" aria-hidden="true"><path d="M8 1 0 8h2v7h4v-4h4v4h4V8h2z"/></svg>
        2815 west Brell ave, Marrowfield Illinois 60948
      </li>
      <li class="contact__item">
        <svg class="contact__icon" viewBox="0 0 16 16" aria-hidden="true"><path d="M1 3h14v10H1z M1 3l7 6 7-6" fill="none" stroke="#aaaaaa" stroke-width="1.6"/></svg>
        Marisjthackery@plumvane.com
      </li>
      <li class="contact__item">
        <svg class="contact__icon" viewBox="0 0 16 16" aria-hidden="true"><path d="M3 1h3l1 4-2 1c1 2 2 3 4 4l1-2 4 1v3c0 1-1 2-2 2C6 14 2 10 1 3c0-1 1-2 2-2z"/></svg>
        3129071436 2815
      </li>
    </ul>

    <div class="accent-band"></div>
  </section>

</body>
</html>
```